Signboard menu for a Fastfood takeaway shop

My current signboard menu is old now, I want to upgrade to a new, bigger and brighter signboard menu.
Photos of the old menu attached but there are some changes in each sections of the menu needs to be changed.
Size of the signboard :
L: 1700cm
H: 1200cm

Industry/Entity Type

Fastfood Hospitality

Colors
FFC000
F8CF3A
FAE287
FDF2CF
FEFAEE

```html
<!DOCTYPE html>
<html lang="en">
<head>
<meta charset="utf-8">
<title>Food Menu Signboard</title>
<link rel="stylesheet" href="https://fonts.googleapis.com/css2?family=Archivo+Black&family=Lexend:wght@400;600;700;800&display=swap">
<style>
  :root {
    --ink: #1d1d1d;
    --amber: #FFC000;
    --sun: #F8CF3A;
    --butter: #FAE287;
    --cream: #FDF2CF;
    --paper: #ffffff;
  }
  * { margin: 0; padding: 0; box-sizing: border-box; }
  html, body { width: 1200px; height: 895px; overflow: hidden; background: var(--paper); }
  body { font-family: "Lexend", sans-serif; color: var(--ink); }
  .board { position: relative; width: 1200px; height: 895px; background: var(--paper); }

  .panel { position: absolute; border-radius: 20px; }
  .panel--yellow { background: var(--sun); }
  .panel--outline { border: 1.2px solid var(--ink); background: var(--paper); }

  .section { position: absolute; top: 0; left: 0; width: 100%; height: 100%; }
  .heading { position: absolute; font-weight: 800; font-size: 20px; line-height: 26px; letter-spacing: -0.4px; text-transform: uppercase; white-space: nowrap; }
  .heading small { font-size: 12px; letter-spacing: -0.2px; }

  .item { position: absolute; font-weight: 600; font-size: 15px; line-height: 18px; letter-spacing: -0.3px; white-space: nowrap; }
  .item--multi { line-height: 16.5px; }
  .item--pack { font-size: 13.5px; line-height: 16.5px; letter-spacing: -0.3px; }
  .price { position: absolute; top: 0; font-weight: 600; }
  .note { position: absolute; font-weight: 400; font-size: 10px; line-height: 12px; white-space: nowrap; }
  .note--tiny { font-size: 8.5px; line-height: 9.5px; }
  .light { font-weight: 400; }

  .divider { position: absolute; height: 1.5px; background: var(--ink); }

  .title { position: absolute; left: 330px; top: 44px; font-family: "Archivo Black", sans-serif; font-size: 80px; line-height: 90px; letter-spacing: -5px; }
  .title-rule { position: absolute; left: 332px; top: 125px; width: 248px; height: 1.5px; background: var(--ink); }
  .tag { position: absolute; font-weight: 800; text-transform: uppercase; white-space: nowrap; }
  .tag--food { left: 307px; top: 45px; width: 71px; height: 29px; background: var(--amber); border: 1px solid var(--ink); font-size: 15px; line-height: 27px; text-align: center; }
  .tag--food-shadow { left: 300px; top: 36px; width: 71px; height: 28px; background: var(--butter); }
  .tag--extras { left: 40px; top: 679px; width: 81px; height: 27px; background: var(--amber); border: 1px solid var(--ink); font-size: 13px; line-height: 25px; text-align: center; }
  .tag--extras-shadow { left: 35px; top: 673px; width: 20px; height: 30px; background: var(--butter); }

  .stamp { position: absolute; background: var(--paper); border: 1px solid var(--ink); font-weight: 800; text-transform: uppercase; line-height: 0.95; letter-spacing: -0.4px; }
  .stamp .accent { color: var(--amber); }
  .stamp--sandwich { left: 36px; top: 543px; width: 224px; height: 52px; transform: rotate(-2.5deg); font-size: 17px; padding: 11px 0 0 12px; }
  .stamp--sandwich .dollar { position: absolute; right: 12px; top: 8px; font-size: 28px; }
  .stamp--hotdog { left: 760px; top: 416px; width: 128px; height: 48px; transform: rotate(-3deg); font-size: 14px; padding: 9px 0 0 10px; }
  .stamp-shadow { position: absolute; left: 758px; top: 409px; width: 126px; height: 10px; background: var(--cream); transform: rotate(-3deg); }
</style>
</head>
<body>
<main class="board">

  <!-- Sandwiches -->
  <div class="panel panel--yellow" style="left:19px;top:18px;width:257px;height:527px;"></div>
  <section class="section sandwiches">
    <h2 class="heading" style="left:39px;top:40px;">Sandwhiches</h2>
    <p class="item" style="left:39px;top:75px;">Baked Beans<span class="price" style="left:165px;">$4.50</span></p>
    <p class="item" style="left:39px;top:100px;">Vegespread<span class="price" style="left:165px;">$3.50</span></p>
    <p class="item" style="left:39px;top:124px;">Cheese<span class="price" style="left:165px;">$3.50</span></p>
    <p class="item" style="left:39px;top:149px;">Tomato<span class="price" style="left:165px;">$3.50</span></p>
    <div class="divider" style="left:48px;top:177px;width:205px;"></div>
    <p class="item" style="left:39px;top:189px;">Salad<span class="price" style="left:165px;">$6.00</span></p>
    <p class="item" style="left:39px;top:214px;">Ham<span class="price" style="left:165px;">$6.50</span></p>
    <p class="item" style="left:39px;top:238px;">Chicken<span class="price" style="left:165px;">$6.50</span></p>
    <p class="item" style="left:39px;top:263px;">Roast Beef<span class="price" style="left:165px;">$6.50</span></p>
    <p class="item" style="left:39px;top:288px;">Salmon<span class="price" style="left:165px;">$6.50</span></p>
    <div class="divider" style="left:48px;top:314px;width:205px;"></div>
    <p class="item" style="left:39px;top:324px;">Tuna<span class="price" style="left:165px;">$6.50</span></p>
    <p class="item" style="left:39px;top:348px;">Rissole<span class="price" style="left:165px;">$6.50</span></p>
    <p class="item" style="left:39px;top:373px;">Sausage<span class="price" style="left:165px;">$6.00</span></p>
    <p class="item" style="left:39px;top:398px;">Scallop<span class="price" style="left:165px;">$5.00</span></p>
    <p class="item" style="left:39px;top:422px;">Chip<span class="price" style="left:165px;">$5.00</span></p>
    <p class="item" style="left:39px;top:447px;">Bacon<span class="price" style="left:165px;">$6.00</span></p>
    <p class="item" style="left:39px;top:472px;">Bacon/Egg<span class="price" style="left:165px;">$6.00</span></p>
    <p class="item" style="left:39px;top:496px;">Schnitzel<span class="price" style="left:165px;">$7.50</span></p>
    <p class="item" style="left:39px;top:521px;">Roll<span class="price" style="left:165px;">30<sup style="font-size:9px;">¢</sup></span></p>
  </section>
  <div class="stamp stamp--sandwich">Or <span class="accent">Create</span><br>Your Own For<span class="dollar">$</span></div>

  <!-- Salads in tubs -->
  <section class="section salads">
    <h2 class="heading" style="left:39px;top:616px;">Salads In Tubs</h2>
    <p class="item" style="left:39px;top:649px;">Plain Or Caesar</p>
    <p class="item" style="left:204px;top:659px;">$8.00</p>
    <div class="tag tag--extras-shadow"></div>
    <div class="tag tag--extras">Extras</div>
    <p class="item" style="left:39px;top:718px;">Egg<span class="price" style="left:165px;">$1.50</span></p>
    <p class="item" style="left:39px;top:743px;">Pineapple<span class="price" style="left:165px;">$0.70</span></p>
    <p class="item" style="left:39px;top:767px;">Avocado<span class="price" style="left:165px;">$1.20</span></p>
    <p class="item" style="left:39px;top:792px;">Cheese<span class="price" style="left:165px;">$1.00</span></p>
    <p class="item" style="left:39px;top:817px;">Bacon/Meat<span class="price" style="left:165px;">$2.50</span></p>
    <p class="item" style="left:39px;top:842px;">Kebab Meat <span class="light" style="font-size:10px;">(Beef)</span><span class="price" style="left:165px;">$3.50</span></p>
    <p class="note" style="left:39px;top:863px;">(Chicken 100g)</p>
    <p class="item" style="left:204px;top:866px;">$4.00</p>
  </section>

  <!-- Title -->
  <div class="tag tag--food-shadow"></div>
  <h1 class="title">MENU</h1>
  <div class="tag tag--food">Food</div>
  <div class="title-rule"></div>

  <!-- Burgers -->
  <section class="section burgers">
    <h2 class="heading" style="left:307px;top:187px;">Burgers <small>(Beef or Chicken)</small></h2>
    <p class="item" style="left:307px;top:226px;">Plain<span class="price" style="left:166px;">$1.50</span></p>
    <p class="item" style="left:307px;top:251px;">Works<span class="price" style="left:166px;">$0.70</span></p>
    <p class="item" style="left:307px;top:275px;">Cheese<span class="price" style="left:166px;">$1.20</span></p>
    <p class="item" style="left:307px;top:300px;">Egg<span class="price" style="left:166px;">$1.00</span></p>
    <p class="item" style="left:307px;top:325px;">Pineapple<span class="price" style="left:166px;">$2.50</span></p>
    <p class="item" style="left:307px;top:350px;">Vegie<span class="price" style="left:166px;">$3.50 / $4.00</span></p>
    <p class="item" style="left:307px;top:374px;">Hawaiion</p>
    <p class="item light" style="left:473px;top:370px;">Beef / Chicken</p>
  </section>

  <!-- Bacon / egg rolls -->
  <div class="panel panel--outline" style="left:307px;top:422px;width:282px;height:224px;"></div>
  <section class="section rolls">
    <h2 class="heading" style="left:327px;top:438px;">Bacon/Egg Rolls</h2>
    <p class="item" style="left:327px;top:472px;">Bacon &amp; Egg<span class="price" style="left:177px;">$7.00</span></p>
    <p class="item item--multi" style="left:327px;top:498px;">Bacon, Egg<br>&amp; Cheese<span class="price" style="left:177px;">$7.50</span></p>
    <p class="item item--multi" style="left:327px;top:539px;">Bacon, Egg,<br>Cheese &amp; Onion<span class="price" style="left:177px;">$7.50</span></p>
    <p class="item item--multi" style="left:327px;top:580px;">Bacon, Egg,<br>Cheese<br>&amp; Avocado<span class="price" style="left:177px;">$8.50</span></p>
  </section>

  <!-- Gravy rolls -->
  <section class="section gravy">
    <h2 class="heading" style="left:327px;top:672px;">Gravy Rolls</h2>
    <p class="item" style="left:327px;top:710px;">Roast Beef<span class="price" style="left:177px;">$8.00</span></p>
    <p class="item" style="left:327px;top:734px;">Chicken<span class="price" style="left:177px;">$7.00</span></p>
    <p class="item" style="left:327px;top:759px;">Rissole<span class="price" style="left:177px;">$7.00</span></p>
    <p class="item" style="left:327px;top:784px;">Sausage<span class="price" style="left:177px;">$6.00</span></p>
    <p class="item" style="left:327px;top:808px;">Schnitzel<span class="price" style="left:177px;">$7.50</span></p>
    <p class="item" style="left:327px;top:833px;">Chip<span class="price" style="left:177px;">$6.50</span></p>
  </section>

  <!-- Kebabs -->
  <div class="panel panel--yellow" style="left:613px;top:18px;width:283px;height:146px;"></div>
  <section class="section kebabs">
    <h2 class="heading" style="left:634px;top:39px;">Kebabs</h2>
    <p class="item" style="left:634px;top:73px;">Lamb<span class="price" style="left:176px;">$14.00</span></p>
    <p class="item" style="left:634px;top:97px;">Mixed<span class="price" style="left:176px;">$14.50</span></p>
    <p class="item" style="left:634px;top:122px;">Chicken<span class="price" style="left:176px;">$12.50</span></p>
  </section>

  <!-- Schnitzel wraps -->
  <section class="section wraps">
    <h2 class="heading" style="left:634px;top:190px;">Schnitzel Wraps</h2>
    <p class="item" style="left:634px;top:224px;">Schnitzel Caesar<span class="price" style="left:176px;">$11.00</span></p>
    <p class="item item--multi" style="left:634px;top:249px;">Schnitzel, Salad<br>&amp; Cheese<span class="price" style="left:176px;">$9.50</span></p>
    <p class="item item--multi" style="left:634px;top:290px;">Schnitzel, Chips<br>&amp; Garlic Sauce<span class="price" style="left:176px;">$9.50</span></p>
    <p class="item" style="left:634px;top:331px;">Schnitzel Works<span class="price" style="left:176px;">$11.50</span></p>
    <p class="note note--tiny" style="left:634px;top:349px;">(Bacon, Egg,<br>Cheese &amp; Salad)</p>
    <p class="item" style="left:634px;top:379px;">Schnitzel Mexican<span class="price" style="left:176px;">$9.50</span></p>
  </section>

  <!-- Hot dogs -->
  <div class="panel panel--yellow" style="left:613px;top:421px;width:283px;height:194px;"></div>
  <section class="section hotdogs">
    <h2 class="heading" style="left:634px;top:441px;">Hot Dogs</h2>
    <p class="item" style="left:634px;top:475px;">Plain<span class="price" style="left:176px;">$6.00</span></p>
    <p class="item" style="left:634px;top:500px;">Cheese<span class="price" style="left:176px;">$6.50</span></p>
    <p class="item" style="left:634px;top:524px;">Cheese &amp; Bacon<span class="price" style="left:176px;">$7.00</span></p>
    <p class="item" style="left:634px;top:549px;">Works<span class="price" style="left:176px;">$8.00</span></p>
    <p class="item" style="left:634px;top:574px;">Double Hotdog<span class="price" style="left:176px;">$9.00</span></p>
  </section>
  <div class="stamp-shadow"></div>
  <div class="stamp stamp--hotdog">Or <span class="accent">Create</span><br>Your Own</div>

  <!-- Big brekky -->
  <section class="section brekky">
    <h2 class="heading" style="left:634px;top:643px;">Big Brekky</h2>
    <p class="item" style="left:634px;top:678px;line-height:16.8px;">Facon, X2 Eggs,<br>Sausage, Fried<br>Tomato, Ash<br>Brown &amp;<br>X2 Slices Toast</p>
    <p class="note" style="left:634px;top:764px;">(With Coffee)</p>
    <p class="item" style="left:810px;top:678px;">$13.00</p>
    <p class="item" style="left:810px;top:760px;">$13.50</p>
    <p class="item" style="left:634px;top:789px;">Snack Packs</p>
    <p class="note" style="left:634px;top:811px;">(Chicken Mixed)</p>
    <p class="note" style="left:634px;top:829px;">(Sauce of your choice)</p>
    <p class="item item--multi" style="left:810px;top:790px;">$14.50/<br>$19.50</p>
    <p class="note" style="left:810px;top:829px;">(Small/Large)</p>
  </section>

  <!-- Hot food -->
  <section class="section hotfood">
    <h2 class="heading" style="left:920px;top:39px;">Hot Food</h2>
    <p class="item" style="left:920px;top:75px;">Scallop<span class="price" style="left:186px;">$2.00</span></p>
    <p class="item" style="left:920px;top:100px;">Dim Sim<span class="price" style="left:186px;">$2.00</span></p>
    <p class="item" style="left:920px;top:125px;">Hash Brown<span class="price" style="left:186px;">$2.50</span></p>
    <p class="item" style="left:920px;top:150px;">Sausage<span class="price" style="left:186px;">$3.00</span></p>
    <p class="item" style="left:920px;top:174px;">Corn Jack<span class="price" style="left:186px;">$3.50</span></p>
    <p class="item" style="left:920px;top:199px;">Rissole<span class="price" style="left:186px;">$4.00</span></p>
    <p class="item" style="left:920px;top:224px;">Chicken Stick<span class="price" style="left:186px;">$3.70</span></p>
    <p class="item" style="left:920px;top:248px;">Crunch Roll<span class="price" style="left:186px;">$3.50</span></p>
    <p class="item" style="left:920px;top:273px;">Spring Roll<span class="price" style="left:186px;">$3.50</span></p>
    <p class="item" style="left:920px;top:298px;">Battered Sav<span class="price" style="left:186px;">$3.50</span></p>
  </section>

  <!-- Seafood -->
  <div class="panel panel--outline" style="left:906px;top:340px;width:283px;height:187px;"></div>
  <section class="section seafood">
    <h2 class="heading" style="left:927px;top:359px;">Seafood</h2>
    <p class="item" style="left:927px;top:391px;">Calamari Rings<span class="price" style="left:185px;top:3px;">$1.50</span></p>
    <p class="item" style="left:927px;top:416px;">Cocktail Fish<span class="price" style="left:185px;top:3px;">$2.50</span></p>
    <p class="item" style="left:927px;top:440px;">Crab Stick<span class="price" style="left:185px;top:3px;">$2.50</span></p>
    <p class="item" style="left:927px;top:465px;">Prawn Cutlet<span class="price" style="left:185px;top:3px;">$2.30</span></p>
    <p class="item" style="left:927px;top:490px;">Battered Fish<span class="price" style="left:185px;top:3px;">$6.50</span></p>
  </section>

  <!-- Seafood pack -->
  <section class="section seafood-pack">
    <h2 class="heading" style="left:927px;top:543px;">Seafood Pack</h2>
    <p class="item item--pack" style="left:927px;top:576px;">1 Lge Fish &amp; Chips<span class="price" style="left:185px;font-size:15px;">$8.00</span></p>
    <p class="item item--pack" style="left:927px;top:601px;">2 Calamari, 2 Prawn<br>Cutlets &amp; Chips<span class="price" style="left:185px;font-size:15px;">$7.00</span></p>
    <p class="item item--pack" style="left:927px;top:642px;">1 Calamari, 1 Prawn<br>Cutlet, 1 Seafood<br>Stick 1 Cocktail<br>Fish &amp; Chips<span class="price" style="left:185px;font-size:15px;">$8.50</span></p>
    <p class="item item--pack" style="left:927px;top:717px;">3 Cocktail<br>Fish &amp; Chips<span class="price" style="left:185px;font-size:15px;">$8.00</span></p>
    <p class="item item--pack" style="left:927px;top:759px;">1 Cocktail Fish, 1 Crab<br>Stick, 2 Prawn Cutlets<br>2 Calamari Rings &amp; Chips<span class="price" style="left:185px;font-size:15px;">$12.50</span></p>
    <p class="item item--pack" style="left:927px;top:816px;">Family... 4 Prawn<br>Cutlets, 6 Cocktail Fish 4<br>Calamari Rings, $4 Chips<br>&amp; 1.25l Drink<span class="price" style="left:194px;font-size:15px;">$34.00</span></p>
  </section>

</main>
</body>
</html>
```